Velvet Harbor Gentlemen's Club 20 YR Anniversary

Need artwork for:
9.65 inches (wide) x 5.34 inches (high) [newspaper ad]
Facebook Cover Photo
Facebook Profile Picture
The design should be consistent throughout the different sizes.

The document attached has the party information.

The party is for our 20 yr anniversary but the highlight of the event is FREE LAP DANCES FOR EVERYBODY
We'd like to use the colors black, red and gold but we are open to any artists thoughts and ideas.

I tried to attach a photo of the guest performer. But when I tried to upload it I received this message: Sorry, you can only upload files up to 4096px in width. At 5616px the file 'IMG_6454edit.jpg' is too wide. I've attached an alternate photo. I hope we can one of them.

Colors
fbed22
ec1f27

Requirements
Must have
• VHG logo
• FREE LAP DANCES FOR EVERYBODY
• No Gimmicks, No Catch...No Strings Attached

```html
<!DOCTYPE html>
<html lang="en">
<head>
<meta charset="utf-8">
<title>VHG 20 Year Anniversary Ad</title>
<link href="https://fonts.googleapis.com/css2?family=Bebas+Neue&family=Lato:wght@400;700;900&display=swap" rel="stylesheet">
<style>
  :root {
    --gold: #fbed22;
    --red: #ec1f27;
    --deep-red: #5e0a0c;
    --black: #050505;
    --white: #ffffff;
    --stage: #2b2b2b;
    --velvet: #6b2a6e;
  }
  * { margin: 0; padding: 0; box-sizing: border-box; }
  html, body { width: 1200px; height: 900px; overflow: hidden; }
  body { background: var(--stage); position: relative; font-family: "Lato", sans-serif; }

  .ad {
    position: absolute; left: 78px; top: 161px;
    width: 1044px; height: 578px;
    background: var(--black); overflow: hidden;
  }
  .ad__left-panel {
    position: absolute; left: 0; top: 0; width: 570px; height: 560px;
    background: radial-gradient(ellipse at 55% 45%, #8a1216 0%, var(--deep-red) 45%, #1a0203 100%);
  }
  .ad__base-strip { position: absolute; left: 0; bottom: 0; height: 16px; }
  .ad__base-strip--white { width: 570px; background: var(--white); }
  .ad__base-strip--red { left: 570px; right: 0; background: var(--red); }

  .performer-photo {
    position: absolute; left: 380px; top: 95px; width: 664px; height: 320px;
    background: radial-gradient(ellipse at 55% 55%, var(--velvet) 0%, #3a1238 40%, rgba(5,5,5,0) 72%);
  }

  .brand-name {
    position: absolute; left: 34px; top: 44px;
    font-family: "Lato", sans-serif; font-weight: 400; font-size: 58px;
    color: var(--red); letter-spacing: -1px; line-height: 1;
  }
  .headline { position: absolute; left: 34px; font-family: "Bebas Neue", sans-serif; line-height: 1; }
  .headline--years { top: 112px; font-size: 112px; color: var(--gold); }
  .headline--anniversary { top: 222px; font-size: 104px; color: var(--white); }

  .offer-bar {
    position: absolute; left: 0; top: 334px; width: 568px; height: 56px;
    background: var(--black);
    font-family: "Bebas Neue", sans-serif; font-size: 46px; line-height: 58px;
    padding-left: 34px; color: var(--white);
  }
  .offer-bar__highlight { color: var(--red); }

  .feature-line {
    position: absolute; left: 0; width: 568px; text-align: center;
    font-family: "Bebas Neue", sans-serif; line-height: 1;
  }
  .feature-line--intro { top: 408px; font-size: 32px; color: var(--gold); }
  .feature-line--star { top: 446px; font-size: 40px; color: var(--white); }

  .venue-address, .venue-site {
    position: absolute; top: 508px; font-size: 20px; color: var(--white);
  }
  .venue-address { left: 30px; }
  .venue-site { left: 397px; }

  .event-date {
    position: absolute; left: 590px; top: 22px; width: 424px; text-align: center;
    font-family: "Bebas Neue", sans-serif; line-height: 1;
  }
  .event-date__day { font-size: 44px; color: var(--white); }
  .event-date__time { font-size: 28px; color: var(--red); margin-top: 2px; }

  .contact { position: absolute; left: 616px; top: 423px; text-align: left; }
  .contact__label { font-weight: 900; font-size: 21px; color: var(--white); }
  .contact__phone { font-family: "Bebas Neue", sans-serif; font-size: 40px; color: var(--red); line-height: 1; }
  .social {
    position: absolute; left: 626px; top: 506px; display: flex; align-items: center; gap: 14px;
    font-size: 21px; color: var(--white);
  }
  .social__mark { width: 22px; height: 22px; background: var(--white); }

  .drink-badge { position: absolute; left: 806px; top: 344px; width: 226px; height: 226px; }
  .drink-badge svg { position: absolute; inset: 0; }
  .drink-badge__text { position: absolute; inset: 0; text-align: center; padding-top: 48px; }
  .drink-badge__price { font-family: "Bebas Neue", sans-serif; font-size: 82px; color: var(--red); line-height: 0.9; }
  .drink-badge__item { font-weight: 900; font-size: 30px; color: #2a1a00; line-height: 1; }
  .drink-badge__note { font-weight: 700; font-size: 19px; color: #2a1a00; }
</style>
</head>
<body>
  <section class="ad">
    <div class="ad__left-panel"></div>
    <div class="performer-photo" role="img" aria-label="Photo of the guest performer posing across a purple tufted armchair"></div>

    <div class="brand-name">VHG</div>
    <h1 class="headline headline--years">20 YEAR</h1>
    <h2 class="headline headline--anniversary">ANNIVERSARY</h2>

    <div class="offer-bar"><span class="offer-bar__highlight">FREE LAPDANCES</span> FOR EVERYONE</div>

    <p class="feature-line feature-line--intro">FEATURING 3 SHOWS WITH</p>
    <p class="feature-line feature-line--star">2015 MISS NUDE WISCONSIN - SCARLET VALE</p>

    <p class="venue-address">2280 Harbor View Rd.&nbsp; Franklin,WI</p>
    <p class="venue-site">www.velvetharbor.club</p>

    <div class="event-date">
      <div class="event-date__day">THURSDAY MAY 12, 2016</div>
      <div class="event-date__time">FROM 6PM UNTIL...</div>
    </div>

    <div class="contact">
      <div class="contact__label">CALL US TODAY</div>
      <div class="contact__phone">414-555-0188</div>
    </div>
    <div class="social"><span class="social__mark"></span>fb/clubvhgwi</div>

    <div class="drink-badge">
      <svg viewBox="0 0 226 226" aria-hidden="true">
        <defs>
          <radialGradient id="badgeGold" cx="50%" cy="50%" r="60%">
            <stop offset="0" stop-color="#fffbc4"/>
            <stop offset="0.55" stop-color="#fbed22"/>
            <stop offset="1" stop-color="#d8a80c"/>
          </radialGradient>
        </defs>
        <g fill="url(#badgeGold)">
          <rect x="38" y="38" width="150" height="150" transform="rotate(0 113 113)"/>
          <rect x="38" y="38" width="150" height="150" transform="rotate(15 113 113)"/>
          <rect x="38" y="38" width="150" height="150" transform="rotate(30 113 113)"/>
          <rect x="38" y="38" width="150" height="150" transform="rotate(45 113 113)"/>
          <rect x="38" y="38" width="150" height="150" transform="rotate(60 113 113)"/>
          <rect x="38" y="38" width="150" height="150" transform="rotate(75 113 113)"/>
        </g>
      </svg>
      <div class="drink-badge__text">
        <div class="drink-badge__price">$3.50</div>
        <div class="drink-badge__item">DRINKS</div>
        <div class="drink-badge__note">ALL NIGHT</div>
      </div>
    </div>

    <div class="ad__base-strip ad__base-strip--white"></div>
    <div class="ad__base-strip ad__base-strip--red"></div>
  </section>
</body>
</html>
```